Mini Leporello with Tartar Recipe from Christmas Apéro

As present from our christmas apero we would like to give our visitors a little booklet of the tartar recipes they enjoyed with us. For this we need a little pocket recipe booklet. ISt should be a Mini-Leparello. You can find the content attached.

Target Market(s)

customers christmas apero

Font styles to use
Other font styles liked:
• FS albert

Requirements
Must have
• each recipe comes from Velmar or Markus Tobler - it should show the author
• the format should be 85 x 85 mm and I need a printable file

```html
<!DOCTYPE html>
<html lang="de">
<head>
<meta charset="utf-8">
<title>Tartar-Rezepte – Weihnachtsapéro Leporello</title>
<link rel="stylesheet" href="https://fonts.googleapis.com/css2?family=Albert+Sans:wght@400;500;700;800&display=swap">
<style>
  :root{
    --stage:#c9cacc;
    --card-dark:#1d1516;
    --band-red:#c4262d;
    --band-red-deep:#7a1419;
    --brand-red:#e53a3c;
    --text:#ffffff;
  }
  *{box-sizing:border-box;margin:0;padding:0}
  html,body{width:767px;height:1200px;overflow:hidden}
  body{background:var(--stage);font-family:"Albert Sans",sans-serif;color:var(--text);position:relative}
  .page{position:absolute;left:110px;width:533px;height:533px;overflow:hidden}
  .page--front{top:36px}
  .page--back{top:614px}
  .page__photo{position:absolute;inset:0;
    background:
      radial-gradient(circle at 20% 30%,rgba(150,110,40,.35),transparent 40%),
      radial-gradient(circle at 80% 60%,rgba(130,30,40,.35),transparent 45%),
      radial-gradient(circle at 45% 85%,rgba(90,60,30,.3),transparent 40%),
      var(--card-dark);}
  .page__frame{position:absolute;left:21px;top:22px;width:491px;height:490px;border:3px solid var(--text)}
  .page__url{position:absolute;left:0;right:0;top:514px;text-align:center;font-size:12px}
  .el{position:absolute;white-space:nowrap}
  .band{position:absolute;left:24px;height:30px;border-radius:0 16px 16px 0;
    background:linear-gradient(90deg,var(--band-red-deep),var(--band-red) 55%,#a81e25);
    font-weight:800;font-size:19px;line-height:30px;padding-left:19px;letter-spacing:.2px}
  .intro{font-size:14px;left:43px}
  .intro--large{font-size:14.5px}
  .intro--compact{font-size:12.5px;letter-spacing:-.1px}
  .intro--tight{font-size:12px;letter-spacing:-.15px}
  .body-copy{left:43px;width:458px;font-size:9.6px;line-height:12.8px;white-space:normal}
  .item{font-size:13px;line-height:15px;display:flex;align-items:flex-start;gap:9px}
  .item svg{width:12px;height:12px;flex:none;margin-top:1px}
  .brand-author{right:32px;font-weight:800;font-size:20px;color:var(--brand-red);letter-spacing:.2px}
  .brand-author--host{display:flex;align-items:center;gap:6px;color:var(--text);font-size:17px}
  .brand-author--host i{width:10px;height:10px;background:var(--brand-red);display:block}
</style>
</head>
<body>
<svg width="0" height="0" style="position:absolute">
  <symbol id="mark" viewBox="0 0 12 12">
    <rect width="12" height="12" fill="#fff"/>
    <path d="M3 3l6 6M9 3l-6 6" stroke="#1d1516" stroke-width="1.6"/>
  </symbol>
</svg>

<!-- Seite 1 -->
<section class="page page--front">
  <div class="page__photo" role="img" aria-label="Dunkles Foto mit weihnachtlichen Lichtern in Bokeh-Unschärfe"></div>
  <div class="page__frame"></div>

  <div class="band" style="top:30px;width:178px">RINDERTARTAR</div>
  <div class="el brand-author brand-author--host" style="top:42px"><i></i>Velmar</div>
  <p class="el intro" style="top:69px">Alle Zutaten fein hacken und mischen:</p>
  <div class="el item" style="left:63px;top:103px"><svg><use href="#mark"/></svg>Rindsfilet</div>
  <div class="el item" style="left:63px;top:126px"><svg><use href="#mark"/></svg>Essiggurken</div>
  <div class="el item" style="left:63px;top:150px"><svg><use href="#mark"/></svg>Oliven</div>
  <div class="el item" style="left:190px;top:101px"><svg><use href="#mark"/></svg>Peperoni</div>
  <div class="el item" style="left:190px;top:126px"><svg><use href="#mark"/></svg>Kapern</div>
  <div class="el item" style="left:190px;top:150px"><svg><use href="#mark"/></svg>Zwiebel</div>
  <div class="el item" style="left:300px;top:101px"><svg><use href="#mark"/></svg>Essig</div>
  <div class="el item" style="left:300px;top:126px"><svg><use href="#mark"/></svg>Senf</div>
  <div class="el item" style="left:391px;top:103px"><svg><use href="#mark"/></svg>Pfeffer</div>
  <div class="el item" style="left:391px;top:124px"><svg><use href="#mark"/></svg>Salz</div>

  <div class="band" style="top:183px;width:313px">LIGURISCHES KALBSTARTAR</div>
  <div class="el brand-author" style="top:184px">Brennwald</div>
  <p class="el intro" style="top:225px">Alle Zutaten fein hacken und mischen:</p>
  <div class="el item" style="left:63px;top:255px"><svg><use href="#mark"/></svg>Kalbfleisch</div>
  <div class="el item" style="left:63px;top:277px"><svg><use href="#mark"/></svg>Zitronen</div>
  <div class="el item" style="left:63px;top:301px"><svg><use href="#mark"/></svg>Olivenoel</div>
  <div class="el item" style="left:190px;top:255px"><svg><use href="#mark"/></svg>Knoblauch</div>
  <div class="el item" style="left:190px;top:278px"><svg><use href="#mark"/></svg>Pfeffer</div>
  <div class="el item" style="left:311px;top:255px"><svg><use href="#mark"/></svg>Salz</div>
  <div class="el item" style="left:311px;top:278px"><svg><use href="#mark"/></svg>Grosszügig<br>Parmesansplitter</div>

  <div class="band" style="top:334px;width:209px">TOMATENTARTAR</div>
  <div class="el brand-author" style="top:334px">Brennwald</div>
  <p class="el body-copy" style="top:375px">Im Prinzip ist das Tomatentartar ein klassisches Rindstartar, anstelle des Fleisches nimmt man einfach getrocknete / in Oel eingelegte Tomaten. Giessen Sie den Grossteils des Oels ab, aber tupfen Sie die Tomaten nicht trocken. Zerkleinern Sie die Tomaten dann mit dem Pürierstab (nicht zu fein) und geben folgende Zutaten hinzu:</p>
  <div class="el item" style="left:63px;top:439px"><svg><use href="#mark"/></svg>Eigelb</div>
  <div class="el item" style="left:63px;top:461px"><svg><use href="#mark"/></svg>Kapern</div>
  <div class="el item" style="left:63px;top:485px"><svg><use href="#mark"/></svg>Basilikum</div>
  <div class="el item" style="left:190px;top:439px"><svg><use href="#mark"/></svg>Cognac</div>
  <div class="el item" style="left:190px;top:462px"><svg><use href="#mark"/></svg>Pfeffer</div>
  <div class="el item" style="left:190px;top:484px"><svg><use href="#mark"/></svg>Salz</div>
  <div class="el item" style="left:311px;top:437px"><svg><use href="#mark"/></svg>Weitere Gewürze nach<br>Abschmecken, bzw. je nach<br>Würzigkeit der im Oel<br>eingelegten Tomaten</div>

  <p class="page__url">www.apero.brennwald-it.ch</p>
</section>

<!-- Seite 2 -->
<section class="page page--back">
  <div class="page__photo" role="img" aria-label="Dunkles Foto mit weihnachtlichen Lichtern in Bokeh-Unschärfe"></div>
  <div class="page__frame"></div>

  <div class="band" style="top:29px;width:280px">THUNATARTAR ASIATISCH</div>
  <div class="el brand-author" style="top:29px">Brennwald</div>
  <p class="el intro intro--compact" style="top:71px">Dieses Thunatartar bekommt mit folgenden Zutaten eine asiatische Note:</p>
  <div class="el item" style="left:63px;top:102px"><svg><use href="#mark"/></svg>Zitronengras</div>
  <div class="el item" style="left:190px;top:101px"><svg><use href="#mark"/></svg>Ingwer</div>
  <div class="el item" style="left:292px;top:101px"><svg><use href="#mark"/></svg>Basilikum</div>
  <div class="el item" style="left:402px;top:102px"><svg><use href="#mark"/></svg>Pfeffer</div>
  <div class="el item" style="left:63px;top:126px"><svg><use href="#mark"/></svg>Etwas Sojasauce mit Wasabi</div>
  <p class="el intro intro--tight" style="top:151px">Fügen Sie weitere asiatische Saucen gemäss Ihrem Geschmack individuell bei.</p>

  <div class="band" style="top:193px;width:166px">LACHSTARTAR</div>
  <div class="el brand-author brand-author--host" style="top:200px"><i></i>Velmar</div>
  <p class="el intro intro--large" style="top:237px">Geräuchter Lachs fein hacken und mit allen Zutaten mischen.</p>
  <div class="el item" style="left:63px;top:266px"><svg><use href="#mark"/></svg>Geräuchter Lachs</div>
  <div class="el item" style="left:200px;top:266px"><svg><use href="#mark"/></svg>Sauerrahm</div>
  <div class="el item" style="left:300px;top:266px"><svg><use href="#mark"/></svg>Dill</div>

  <div class="band" style="top:317px;width:154px">KÄSETARTAR</div>
  <div class="el brand-author brand-author--host" style="top:320px"><i></i>Velmar</div>
  <p class="el body-copy" style="top:357px">Den Käse entrinden und in kleine Würfelchen schneiden, Lauch blanchieren, kalt abschrecken. Petersilie und Radieschen hacken danach alle Zutaten mischen und anrichten.</p>
  <div class="el item" style="left:63px;top:399px"><svg><use href="#mark"/></svg>Halbhartkäse</div>
  <div class="el item" style="left:63px;top:421px"><svg><use href="#mark"/></svg>Weinessig</div>
  <div class="el item" style="left:63px;top:444px"><svg><use href="#mark"/></svg>Basilikum</div>
  <div class="el item" style="left:63px;top:469px"><svg><use href="#mark"/></svg>Rahm</div>
  <div class="el item" style="left:190px;top:399px"><svg><use href="#mark"/></svg>Radieschen</div>
  <div class="el item" style="left:190px;top:422px"><svg><use href="#mark"/></svg>Senf</div>
  <div class="el item" style="left:190px;top:444px"><svg><use href="#mark"/></svg>Salz</div>
  <div class="el item" style="left:292px;top:397px"><svg><use href="#mark"/></svg>Petersilie<br>Glattblätterig</div>
  <div class="el item" style="left:292px;top:431px"><svg><use href="#mark"/></svg>Schwarzer<br>Pfeffer</div>
  <div class="el item" style="left:402px;top:398px"><svg><use href="#mark"/></svg>Lauch</div>
  <div class="el item" style="left:402px;top:431px"><svg><use href="#mark"/></svg>Rapsöl</div>

  <p class="page__url">www.apero.brennwald-it.ch</p>
</section>
</body>
</html>
```